TK & LJ Shearing Pty Ltd

We already have an existing logo created by Lumen Guild however we have restructured to a company. We would like someone to add Pty Ltd to our business name please.

Colors

Designer to choose only greyscale colors for use in the design.

```html
<!DOCTYPE html>
<html lang="en">
<head>
<meta charset="utf-8">
<title>TK &amp; LJ Shearing Pty Ltd – Business Card</title>
<link href="https://fonts.googleapis.com/css2?family=Tinos:wght@400;700&display=swap" rel="stylesheet">
<style>
  :root {
    --page: #ffffff;
    --card: #000000;
    --ink: #ffffff;
  }
  html, body {
    margin: 0;
    padding: 0;
    width: 1200px;
    height: 702px;
    overflow: hidden;
    background: var(--page);
  }
  .canvas {
    position: relative;
    width: 1200px;
    height: 702px;
    background: var(--page);
  }
  .card {
    position: absolute;
    left: 170px;
    top: 99px;
    width: 866px;
    height: 507px;
    background: var(--card);
    font-family: "Tinos", "Times New Roman", serif;
    color: var(--ink);
  }
  .brand-lockup {
    position: absolute;
    left: 172px;
    top: 105px;
    display: flex;
    align-items: center;
    gap: 22px;
  }
  .brand-lockup__dot {
    width: 110px;
    height: 110px;
    border-radius: 50%;
    background: var(--ink);
    flex: none;
  }
  .brand-lockup__name {
    margin: 0;
    font-size: 54px;
    font-weight: 700;
    line-height: 70px;
    color: var(--ink);
  }
  .brand-lockup__name span {
    display: block;
  }
  .company-suffix {
    position: absolute;
    left: 677px;
    top: 222px;
    font-size: 29px;
    font-weight: 700;
    letter-spacing: 0.5px;
  }
  .contact-list {
    position: absolute;
    left: 71px;
    top: 344px;
    margin: 0;
    padding: 0;
    list-style: none;
  }
  .contact-item {
    display: flex;
    align-items: center;
    height: 38.5px;
    font-size: 25px;
    letter-spacing: 0.4px;
  }
  .contact-icon {
    width: 31px;
    height: 31px;
    margin-right: 16px;
    flex: none;
  }
</style>
</head>
<body>
<div class="canvas">
  <section class="card">
    <div class="brand-lockup" role="img" aria-label="TK &amp; LJ Shearing logo">
      <div class="brand-lockup__dot"></div>
      <h1 class="brand-lockup__name">
        <span>TK &amp; LJ</span>
        <span>SHEARING</span>
      </h1>
    </div>
    <span class="company-suffix">PTY LTD</span>

    <ul class="contact-list">
      <li class="contact-item">
        <svg class="contact-icon" viewBox="0 0 32 32" aria-hidden="true">
          <circle cx="16" cy="16" r="15" fill="var(--ink)"/>
          <path d="M16 7 L6 16 H9 V25 H14 V19 H18 V25 H23 V16 H26 Z" fill="var(--card)"/>
        </svg>
        Po Box 418 MERREDIN WA 6415
      </li>
      <li class="contact-item">
        <svg class="contact-icon" viewBox="0 0 32 32" aria-hidden="true">
          <circle cx="16" cy="16" r="15" fill="var(--ink)"/>
          <path d="M10.5 7.5 C9 8 7.5 9.5 7.8 12 C8.5 17.5 14.5 23.5 20 24.2 C22.5 24.5 24 23 24.5 21.5 L21.2 18.6 C20.5 18 19.6 18.2 19 18.9 L18 20 C15.6 18.8 13.2 16.4 12 14 L13.1 13 C13.8 12.4 14 11.5 13.4 10.8 Z" fill="var(--card)"/>
        </svg>
        Tom 0491570156
      </li>
      <li class="contact-item">
        <svg class="contact-icon" viewBox="0 0 32 32" aria-hidden="true">
          <circle cx="16" cy="16" r="15" fill="var(--ink)"/>
          <rect x="8" y="10.5" width="16" height="11" fill="none" stroke="var(--card)" stroke-width="1.8"/>
          <path d="M8 10.5 L16 17 L24 10.5" fill="none" stroke="var(--card)" stroke-width="1.8"/>
        </svg>
        tkljshearing@mailbox.net
      </li>
    </ul>
  </section>
</div>
</body>
</html>
```